Packaging design for high end, natural skin care line needed

Marisol Thackery Beauty needs a label design. It is a new skin care line I am launching.
For years my line Velvet Orchard Beauty was quite popular and featured in several magazines, but for personal reasons had to be shut down. Now I am launching a new line featuring VOB's top selling products, but focused solely on skin care more so than cosmetics. All products will still be handmade, but the line should still look professional-something worthy of a Brindle Market shelf!
I am branding it with my name, as I am often quoted in articles related to gluten in beauty products, so Marisol Thackery and beauty are key words.
The key products will be facial and body serums which are packaged in .5oz., 1oz. and larger amber glass bottles with black dropper tops, I will include pictures below. For dimensions, the labels can be any size that you think will work best, but need to at the least fit the 1oz. bottle, dimensions shown here http://www.corvelflask.example/amber-glass-tall-round-flask/p/QZ7K-93/
I loved the former VOB logo, but for Marisol Thackery Beauty I am looking for something more personal, more apothecary-like, and probably less colorful.
The line will be small, just a handful of products, but luxe, rich.
I am attaching photos of Velvet Orchard Beauty's packaging for your reference.
Thanks much!!

Hi Everyone! Thank you for your submissions! Please see the links I provided in the brief, I really am looking for something more technical looking, like an apothecary. And want black text on a white background, not a black background, and nothing flowery.
Thank you all!!
Marisol

Target Market(s)

My clients are primarily women of all ages, but with more of a skin care focus, and no longer a cosmetic one, I would also like to appeal to a male audience. My clients are health conscious, gluten-free, natural, paleo, or vegan, etc. Target age is probably 25-55. Products are a bit high end, priced $45-65.

Industry/Entity Type

Cosmetics

Requirements
Must have
• It must at least say Marisol Thackery, or can say Marisol Thackery Beauty, but "Beauty" is not necessary. And capitalization is open, try whatever you think serves the brand. Likely slogans or taglines that can be included but are not essential: Care for your skin. Love and care for your skin. Handmade with love in the USA. Handmade in the USA. Think modern day apothecary. Small batch scotch. Something fine, but custom, handmade.
Nice to have
• I like the aesthetic of Oribel Skin Care a bit http://www.oribelhollis.example.au/
And of Dorian Valtz as shown here http://www.pinboardia.example/pin/847302915563017442/
Also of something like this that is even customizable http://www.pinboardia.example/pin/58274106392285514/
Every product is handmade in small batches, with fine ingredients, a moderate price point of around $45-$65. And I will likely begin making custom orders. So there could be a space to say when it was made, or for whom. I would like to keep the colors classic though, I probably want to stay away from the bright pink on this one.
Should not have
• As I mentioned, probably want to stay away from a lot of color. I like black vs. gray for the text, as it will show up better in editorials. I must look good, but also photograph well. Thanks!

```html
<!DOCTYPE html>
<html lang="en">
<head>
<meta charset="utf-8">
<title>Marisol Thackery Beauty – Serum Label</title>
<link rel="stylesheet" href="https://fonts.googleapis.com/css2?family=Raleway:wght@400&family=Libre+Baskerville&display=swap">
<style>
  :root {
    --backdrop: #ededed;
    --backdrop-center: #fafafa;
    --label-paper: #ffffff;
    --ink: #4a4240;
    --ink-soft: #6e6664;
    --rule: #8a8280;
    --mark-fill: #9a9290;
  }
  * { box-sizing: border-box; margin: 0; padding: 0; }
  html, body { width: 1200px; height: 900px; overflow: hidden; }
  body {
    background: radial-gradient(ellipse at 50% 45%, var(--backdrop-center) 0%, var(--backdrop) 75%);
    font-family: "Raleway", "Helvetica Neue", Arial, sans-serif;
    color: var(--ink);
    position: relative;
  }
  .label {
    position: absolute;
    left: 150px;
    top: 170px;
    width: 900px;
    height: 340px;
    background: var(--label-paper);
    box-shadow: 0 2px 8px rgba(0,0,0,0.12);
  }
  .label-frame-outer {
    position: absolute;
    inset: 10px;
    border: 4px solid var(--ink);
  }
  .label-frame-inner {
    position: absolute;
    inset: 20px;
    border: 1.5px solid var(--ink);
  }
  .side-copy {
    position: absolute;
    left: 38px;
    top: 50%;
    width: 250px;
    transform: translate(-50%, -50%) rotate(90deg);
    transform-origin: center;
    margin-left: 14px;
    font-family: "Libre Baskerville", Georgia, serif;
    font-size: 7px;
    line-height: 12px;
    letter-spacing: 0.3px;
    color: var(--ink);
    text-transform: uppercase;
    white-space: nowrap;
  }
  .brand-block {
    position: absolute;
    left: 0;
    right: 0;
    top: 52px;
    display: flex;
    flex-direction: column;
    align-items: center;
  }
  .top-rule {
    width: 290px;
    height: 0;
    border-top: 1.5px solid var(--rule);
    margin-bottom: 22px;
  }
  .brand-dot {
    width: 74px;
    height: 74px;
    border-radius: 50%;
    background: var(--mark-fill);
    margin-bottom: 18px;
  }
  .brand-name {
    font-size: 23px;
    font-weight: 400;
    letter-spacing: 1px;
    color: var(--ink-soft);
    margin-bottom: 18px;
  }
  .beauty-line {
    display: flex;
    align-items: center;
    gap: 10px;
  }
  .beauty-line .rule {
    width: 92px;
    border-top: 1.5px solid var(--rule);
  }
  .beauty-line .word {
    font-size: 8px;
    letter-spacing: 3px;
    color: var(--ink-soft);
    text-transform: uppercase;
  }
  .volume {
    position: absolute;
    right: 110px;
    bottom: 52px;
    font-family: "Libre Baskerville", Georgia, serif;
    font-size: 14px;
    color: var(--ink);
  }
  .lockup {
    position: absolute;
    right: 150px;
    bottom: 70px;
    display: flex;
    flex-direction: column;
    align-items: center;
  }
  .lockup .brand-dot {
    width: 96px;
    height: 96px;
    margin-bottom: 24px;
  }
  .lockup-name {
    font-size: 28px;
    letter-spacing: 2px;
    color: var(--ink-soft);
  }
</style>
</head>
<body>
  <section class="label" aria-label="Serum bottle label">
    <div class="label-frame-outer"></div>
    <div class="label-frame-inner"></div>
    <p class="side-copy">Handmade in small batches with fine oils, USA.<br>Apply two drops to clean skin, morning and night.</p>
    <div class="brand-block">
      <div class="top-rule"></div>
      <div class="brand-dot"></div>
      <p class="brand-name">MarisolThackery</p>
      <div class="beauty-line">
        <span class="rule"></span>
        <span class="word">Beauty</span>
        <span class="rule"></span>
      </div>
    </div>
    <p class="volume">1.5oz</p>
  </section>

  <div class="lockup" aria-label="Brand name lockup">
    <div class="brand-dot"></div>
    <p class="lockup-name">MarisolThackery</p>
  </div>
</body>
</html>
```